Business Card Design

Our Motto is "Protecting Australia's Underground Utilities"

We want the Southern Cross inside a shield I have attached the southern cross and our old shield design

Product description is: Vacuum Excavation & Utility Location
Wet & Dry Vacuum Loading
Confined Space Entry Specialists
High Pressure Cleaning

The Southern Cross in the shield must be blue and white. The Company name must be Coastal Pipeline Guard. The Green & Gold Shield logo I uploaded is my OLD logo design. Thank you

Target Market(s)

Civil Construction

Industry/Entity Type

Business

Contact Information for Business Card

Coastal Pipeline Guard Pty Ltd
Corey Hallworth(Director)
0413862051
coreyh@pipeguardco.com.au
A.B.N.52938407716

Colors
0456a3

Requirements
Must have
• Southern Cross inside a shield, Blue and white design on the Southern Cross shield.
Must say Coastal Pipeline Guard P/L

```html
<!DOCTYPE html>
<html lang="en">
<head>
<meta charset="utf-8">
<title>Coastal Pipeline Guard – Business Card</title>
<link href="https://fonts.googleapis.com/css2?family=Montserrat:wght@500;700;800&display=swap" rel="stylesheet">
<style>
  :root {
    --sky-light: #8ff0ff;
    --sky-mid: #33d6f7;
    --sky-deep: #0a7df2;
    --royal: #0b3fe0;
    --navy: #0a1fb8;
    --mark: #0a2fd6;
    --white: #ffffff;
    --ink: #000000;
    --label: #e6fbff;
  }
  * { box-sizing: border-box; margin: 0; padding: 0; }
  html, body { width: 1200px; height: 742px; overflow: hidden; background: var(--white); }
  .card {
    position: relative;
    width: 1200px;
    height: 742px;
    overflow: hidden;
    font-family: "Montserrat", Arial, sans-serif;
    background: var(--white);
    border: 4px solid var(--ink);
  }
  .card__background {
    position: absolute;
    left: 16px; top: 16px;
    width: 1160px; height: 702px;
    border: 2px solid var(--ink);
    display: block;
  }
  .holder-name {
    position: absolute;
    top: 28px; left: 0; width: 100%;
    text-align: center;
    font-weight: 800;
    font-size: 50px;
    line-height: 56px;
    letter-spacing: 3px;
    color: var(--royal);
  }
  .holder-role {
    position: absolute;
    top: 86px; left: 0; width: 100%;
    text-align: center;
    font-weight: 500;
    font-size: 29px;
    line-height: 34px;
    letter-spacing: 4px;
    color: var(--label);
  }
  .contact-phone {
    position: absolute;
    top: 125px; left: 344px;
    display: flex; align-items: center; gap: 16px;
    font-weight: 500;
    font-size: 40px;
    line-height: 54px;
    letter-spacing: 6px;
    color: var(--royal);
  }
  .icon-tile { width: 54px; height: 54px; display: block; flex: none; }
  .brand-mark {
    position: absolute;
    top: 200px; left: 0; width: 100%;
    display: flex; flex-direction: column; align-items: center; gap: 22px;
  }
  .brand-mark__circle {
    width: 170px; height: 170px;
    border-radius: 50%;
    background: var(--mark);
  }
  .brand-mark__name {
    font-weight: 700;
    font-size: 30px;
    line-height: 36px;
    letter-spacing: 3px;
    color: var(--mark);
  }
  .company-name {
    position: absolute;
    top: 504px; left: 0; width: 100%;
    text-align: center;
    font-weight: 500;
    font-size: 42px;
    line-height: 37px;
    letter-spacing: 4px;
    color: var(--royal);
  }
  .contact-footer {
    position: absolute;
    top: 664px; left: 30px;
    display: flex; align-items: center; gap: 12px;
    font-weight: 500;
    font-size: 30px;
    line-height: 54px;
    letter-spacing: 2.5px;
    color: var(--white);
  }
  .contact-footer .abn { margin-left: 40px; }
</style>
</head>
<body>
<div class="card">
  <svg class="card__background" viewBox="0 0 1160 702" preserveAspectRatio="none" aria-hidden="true">
    <defs>
      <radialGradient id="glow" cx="0.48" cy="0.3" r="0.75">
        <stop offset="0" stop-color="#b8fbff"/>
        <stop offset="0.45" stop-color="#4fe0fb"/>
        <stop offset="1" stop-color="#14b4f0"/>
      </radialGradient>
      <linearGradient id="swoopRight" x1="0" y1="0" x2="1" y2="0">
        <stop offset="0" stop-color="#1aa8f5"/>
        <stop offset="1" stop-color="#0a6ef0"/>
      </linearGradient>
      <linearGradient id="swoopLeft" x1="0" y1="0" x2="1" y2="1">
        <stop offset="0" stop-color="#0a7df2"/>
        <stop offset="1" stop-color="#35c8f6"/>
      </linearGradient>
    </defs>
    <rect width="1160" height="702" fill="url(#glow)"/>
    <path d="M1000 0 C880 120 900 420 760 560 C660 660 560 702 520 702 L1160 702 L1160 0 Z" fill="url(#swoopRight)" opacity="0.85"/>
    <path d="M1060 0 C960 140 990 420 860 560 C780 650 700 702 680 702 L1160 702 L1160 0 Z" fill="#0b66ee" opacity="0.6"/>
    <path d="M1010 20 C930 160 960 400 830 560" fill="none" stroke="#7fe4ff" stroke-width="6" opacity="0.6"/>
    <path d="M0 250 C60 160 180 60 300 0 L0 0 Z" fill="#7eeafc" opacity="0.5"/>
    <path d="M0 330 C80 420 60 560 0 640 Z" fill="url(#swoopLeft)" opacity="0.8"/>
    <path d="M0 702 C120 520 140 330 300 180 C380 110 460 60 520 40" fill="none" stroke="#6fe6ff" stroke-width="10" opacity="0.55"/>
    <path d="M60 702 C170 520 190 360 340 220" fill="none" stroke="#1c8ff2" stroke-width="4" opacity="0.5"/>
  </svg>

  <h1 class="holder-name">COREY HALLWORTH</h1>
  <p class="holder-role">DIRECTOR</p>

  <p class="contact-phone">
    <svg class="icon-tile" viewBox="0 0 54 54" aria-hidden="true">
      <rect x="2" y="2" width="50" height="50" rx="10" fill="#1196f0" stroke="#7fd8ff" stroke-width="2"/>
      <rect x="9" y="9" width="36" height="36" rx="6" fill="#e9fbff"/>
      <path d="M19 15 l5 0 2 7 -3 3 c2 4 4 6 8 8 l3 -3 7 2 0 5 c-1 2 -3 3 -5 3 c-10 -1 -19 -10 -20 -20 c0 -2 1 -4 3 -5 z" fill="#1a6fd8"/>
    </svg>
    <span>0413862051</span>
  </p>

  <div class="brand-mark">
    <span class="brand-mark__circle" aria-hidden="true"></span>
    <p class="brand-mark__name">COASTAL PIPELINE GUARD</p>
  </div>

  <p class="company-name">COASTAL<br>PIPELINE<br>GUARD<br>P/L</p>

  <p class="contact-footer">
    <svg class="icon-tile" viewBox="0 0 54 54" aria-hidden="true">
      <rect x="2" y="2" width="50" height="50" rx="10" fill="#1196f0" stroke="#7fd8ff" stroke-width="2"/>
      <text x="27" y="36" text-anchor="middle" font-family="Montserrat, Arial, sans-serif" font-size="26" font-weight="700" fill="#ffffff">@</text>
    </svg>
    <span class="email">coreyh@pipeguardco.com.au</span>
    <span class="abn">A.B.N.52938407716</span>
  </p>
</div>
</body>
</html>
```